Fun, Clean Business Card For Family Focused Travel Agency

I need a business card using specific colors and fonts as in the uploaded files. Ideally, I would like a large image of the logo on the back and all the contact info on the front. Maybe the stars/dots somewhere in a flowy form.

I do want it the contact information to be clear and easy to read. I don't want it to look too busy. Maybe even a bit minimalist.

I plan or ordering the ROUNDED CORNER business cards from Cardloom, so please consider that in your design.

Target Market(s)

Families with children, couples, groups of friends

Contact Information for Business Card

Marisol Trent, Owner
Marisol@BreezeTrips.example
Cell Phone Number 555-218-4637
Office Phone Number 555-762-1094
Specializing in Fablewood destinations, Grandvista Lakeside Park, Cruises and All-Inclusive Vacations.

Nice but not required:
www.BreezeTrips.example
Facebook, Instagram, Twitter icons with username: BreezeTrips

Font styles to use
Sans Serif

Requirements
Must have
• Please try to use the colors from the logo as much as possible. I understand lighter shades/colors may be needed for some things.
Should not have
• NO SERIF FONTS. That is really the only thing I do not want at all

```html
<!DOCTYPE html>
<html lang="en">
<head>
<meta charset="utf-8">
<title>Breeze Trips – Business Card</title>
<link href="https://fonts.googleapis.com/css2?family=Arimo:ital,wght@0,400;0,700;1,400&display=swap" rel="stylesheet">
<style>
  :root {
    --backdrop: #33b493;
    --card: #ffffff;
    --ink: #14182b;
    --teal: #21b8a0;
    --orange: #e8752a;
    --rule: #8a8a8a;
    --sparkle-blue: #bfe3f2;
    --sparkle-gold: #f6e6b8;
    --sparkle-peach: #f7d6c4;
  }
  * { margin: 0; padding: 0; box-sizing: border-box; }
  html, body {
    width: 1200px;
    height: 849px;
    overflow: hidden;
    background: var(--backdrop);
    font-family: "Arimo", Arial, sans-serif;
    color: var(--ink);
  }
  .stage { position: relative; width: 1200px; height: 849px; }

  .card {
    position: absolute;
    width: 604px;
    height: 345px;
    background: var(--card);
    border-radius: 20px;
    overflow: hidden;
  }
  .card--back { left: 120px; top: 110px; }
  .card--front { left: 476px; top: 396px; }

  /* Back: brand name */
  .brand {
    position: absolute;
    left: 0; right: 0; top: 0; bottom: 0;
    display: flex;
    align-items: center;
    justify-content: center;
    gap: 22px;
    padding-bottom: 10px;
  }
  .brand__dot {
    width: 40px;
    height: 40px;
    border-radius: 50%;
    background: var(--orange);
    flex: none;
  }
  .brand__name {
    font-size: 62px;
    font-weight: 700;
    color: var(--ink);
    letter-spacing: -0.5px;
    white-space: nowrap;
  }

  /* Front: contact */
  .sparkle-trail {
    position: absolute;
    left: 50px;
    top: 140px;
    width: 510px;
    height: 80px;
    border-radius: 40px;
    background: linear-gradient(90deg,
      var(--sparkle-blue) 0%,
      var(--sparkle-peach) 30%,
      rgba(255,255,255,0) 50%,
      var(--sparkle-gold) 75%,
      var(--sparkle-blue) 100%);
    opacity: 0.35;
  }
  .contact {
    position: absolute;
    left: 0; right: 0; top: 0;
    text-align: center;
  }
  .contact__name {
    position: absolute;
    left: 0; right: 0; top: 30px;
    font-size: 24px;
    font-weight: 700;
  }
  .contact__title {
    position: absolute;
    left: 0; right: 0; top: 60px;
    font-size: 17px;
  }
  .contact__rule {
    position: absolute;
    left: 108px;
    width: 392px;
    top: 101px;
    height: 0;
    border-top: 1px solid var(--rule);
  }
  .contact__phones {
    position: absolute;
    left: 0; right: 0; top: 133px;
    font-size: 20px;
    line-height: 24px;
  }
  .contact__email {
    position: absolute;
    left: 0; right: 0; top: 200px;
    font-size: 20px;
  }
  .contact__specialty {
    position: absolute;
    left: 0; right: 0; top: 272px;
    font-size: 12.5px;
    font-style: italic;
    line-height: 18px;
  }
</style>
</head>
<body>
<main class="stage">
  <section class="card card--back" aria-label="Card back">
    <div class="brand">
      <span class="brand__dot"></span>
      <span class="brand__name">Breeze Trips</span>
    </div>
  </section>

  <section class="card card--front" aria-label="Card front">
    <div class="sparkle-trail" role="img" aria-label="Faint flowing trail of small coloured stars and dots"></div>
    <div class="contact">
      <p class="contact__name">Marisol Trent</p>
      <p class="contact__title">Owner</p>
      <span class="contact__rule"></span>
      <p class="contact__phones">Cell: 555-218-4637<br>Office:555-762-1094</p>
      <p class="contact__email">Marisol@BreezeTrips.example</p>
      <p class="contact__specialty">Specializing in Fablewood destinations, Grandvista Lakeside Park,<br>Cruises and All-Inclusive Vacations.</p>
    </div>
  </section>
</main>
</body>
</html>
```